Maple & Fig Business Card FUN & EXCITING

Here is the Information for the Card:
Harvinder Gill (Raj)
E: RajGill@postmeadow.com
C: (480) 730-9146
www.MapleFigLV.com

We don't want traditional Indian cliche, We a playful bold and fun business card.

Files: https://files.cloudvessel.com/folders/7TqRmXa2Lp9KzVb4Hn8YcW3EuJd6FsGo?usp=share_link

https://files.cloudvessel.com/folders/3PzLkQw8Rt5MnXc2Vb7JhY4GsDf9AeUo?usp=share_link

Target Market(s)

Las Vegas Local Restaurant

Industry/Entity Type

Indian Restaurant

Contact Information for Business Card

Name, Email, Cell Phone, Company Logo

```html
<!DOCTYPE html>
<html lang="en">
<head>
<meta charset="utf-8">
<title>Maple &amp; Fig — Business Card</title>
<link rel="stylesheet" href="https://fonts.googleapis.com/css2?family=Source+Sans+3:wght@400;600;700;900&family=Quicksand:wght@500;600;700&display=swap">
<style>
  :root {
    --stage: #8c8c8c;
    --paper: #ffffff;
    --raspberry: #e0195a;
    --saffron: #f0b323;
    --teal: #0fae94;
    --ink: #1d1f4b;
    --black: #111111;
    --note: #ffffff;
  }
  * { box-sizing: border-box; margin: 0; padding: 0; }
  html, body { width: 1200px; height: 1200px; overflow: hidden; }
  body {
    position: relative;
    background: var(--stage);
    font-family: "Quicksand", sans-serif;
  }
  .card {
    position: absolute;
    left: 226px;
    width: 746px;
    height: 435px;
    box-shadow: 0 18px 40px rgba(0,0,0,0.35);
  }
  .card--front { top: 91px; background: var(--paper); }
  .card--back  { top: 601px; background: var(--raspberry); overflow: hidden; }

  /* front: brand block */
  .brand {
    position: absolute;
    left: 40px; top: 44px;
    width: 290px;
    text-align: center;
  }
  .brand__name {
    font-family: "Source Sans 3", sans-serif;
    font-weight: 900;
    font-size: 58px;
    line-height: 1;
    color: var(--black);
    letter-spacing: -1px;
  }
  .brand__place {
    font-family: "Source Sans 3", sans-serif;
    font-weight: 700;
    font-size: 17px;
    color: var(--black);
    margin-top: 8px;
    text-align: right;
    padding-right: 8px;
  }
  .brand__art {
    display: block;
    margin: 8px auto 0;
    width: 270px;
    height: 170px;
  }
  .brand__tagline {
    font-family: "Source Sans 3", sans-serif;
    font-size: 15px;
    font-weight: 600;
    color: var(--black);
    margin-top: 10px;
  }

  .divider {
    position: absolute;
    left: 380px; top: 50px;
    width: 3px; height: 334px;
    background: var(--teal);
  }

  /* front: contact block */
  .contact {
    position: absolute;
    left: 383px; right: 0; top: 100px;
    text-align: center;
  }
  .contact__name {
    font-family: "Source Sans 3", sans-serif;
    font-weight: 600;
    font-size: 38px;
    line-height: 1.1;
    color: var(--raspberry);
  }
  .contact__nickname {
    font-family: "Source Sans 3", sans-serif;
    font-weight: 600;
    font-size: 30px;
    line-height: 1.2;
    color: var(--saffron);
  }
  .contact__icons {
    display: flex;
    justify-content: center;
    gap: 4px;
    margin: 12px 0 14px;
  }
  .contact__icon { width: 42px; height: 42px; }
  .contact__lines {
    list-style: none;
    font-weight: 500;
    font-size: 23px;
    line-height: 31px;
    color: var(--ink);
  }

  /* back */
  .back__name {
    position: absolute;
    left: 0; right: 0; top: 40px;
    text-align: center;
    font-family: "Source Sans 3", sans-serif;
    font-weight: 900;
    font-size: 128px;
    line-height: 120px;
    color: var(--paper);
    text-transform: uppercase;
    letter-spacing: 2px;
  }
  .back__band {
    position: absolute;
    left: 192px; top: 298px;
    width: 384px; height: 124px;
  }
  .back__band-label {
    position: absolute;
    left: 192px; top: 322px;
    width: 384px;
    text-align: center;
    font-weight: 700;
    font-size: 50px;
    line-height: 70px;
    color: var(--paper);
  }

  /* font notes */
  .note {
    position: absolute;
    color: var(--note);
  }
  .note--heading {
    left: 991px; top: 152px;
    font-family: "Source Sans 3", sans-serif;
    font-weight: 700;
    font-size: 32px;
  }
  .note--body {
    left: 996px; top: 314px;
    font-family: "Quicksand", sans-serif;
    font-weight: 500;
    font-size: 28px;
  }
  .note-arrow { position: absolute; width: 60px; height: 60px; }
  .note-arrow--heading { left: 985px; top: 200px; }
  .note-arrow--body { left: 985px; top: 356px; }
</style>
</head>
<body>

<section class="card card--front">
  <div class="brand">
    <div class="brand__name">Maple &amp; Fig</div>
    <div class="brand__place">Las Vegas, NV</div>
    <svg class="brand__art" viewBox="0 0 270 170" role="img" aria-label="Illustration of a cheerful curry bowl and naan walking together with hearts and sparkles">
      <defs>
        <linearGradient id="artTone" x1="0" y1="0" x2="1" y2="1">
          <stop offset="0" stop-color="#f6d9c4"/>
          <stop offset="0.55" stop-color="#f2a25c"/>
          <stop offset="1" stop-color="#e88aa8"/>
        </linearGradient>
      </defs>
      <rect x="0" y="0" width="270" height="170" rx="14" fill="url(#artTone)"/>
    </svg>
    <div class="brand__tagline">“A match made in heaven”</div>
  </div>

  <div class="divider"></div>

  <div class="contact">
    <div class="contact__name">Harvinder Gill</div>
    <div class="contact__nickname">(Raj)</div>
    <div class="contact__icons">
      <svg class="contact__icon" viewBox="0 0 42 42" aria-label="Phone">
        <circle cx="21" cy="21" r="20" fill="var(--teal)"/>
        <rect x="15" y="10" width="12" height="22" rx="2" fill="none" stroke="#fff" stroke-width="2"/>
        <line x1="19" y1="28.5" x2="23" y2="28.5" stroke="#fff" stroke-width="2"/>
      </svg>
      <svg class="contact__icon" viewBox="0 0 42 42" aria-label="Email">
        <circle cx="21" cy="21" r="20" fill="var(--teal)"/>
        <rect x="10" y="13" width="22" height="16" rx="1.5" fill="none" stroke="#fff" stroke-width="2"/>
        <polyline points="10,14 21,23 32,14" fill="none" stroke="#fff" stroke-width="2"/>
      </svg>
      <svg class="contact__icon" viewBox="0 0 42 42" aria-label="Website">
        <circle cx="21" cy="21" r="20" fill="var(--teal)"/>
        <g fill="none" stroke="#fff" stroke-width="1.8">
          <circle cx="21" cy="21" r="11"/>
          <ellipse cx="21" cy="21" rx="5" ry="11"/>
          <line x1="10" y1="21" x2="32" y2="21"/>
          <path d="M12 15.5h18M12 26.5h18"/>
        </g>
      </svg>
    </div>
    <ul class="contact__lines">
      <li>(480) 730-9146</li>
      <li>rajgill@postmeadow.com</li>
      <li>maplefiglv.com</li>
    </ul>
  </div>
</section>

<section class="card card--back">
  <div class="back__name">Maple<br>&amp; Fig</div>
  <svg class="back__band" viewBox="0 0 384 124" aria-hidden="true">
    <polygon points="4,22 376,0 384,92 0,124" fill="var(--teal)"/>
  </svg>
  <div class="back__band-label">INDIAN GRUB</div>
</section>

<div class="note note--heading">Source Sans</div>
<svg class="note-arrow note-arrow--heading" viewBox="0 0 60 60" aria-hidden="true">
  <path d="M44 4 C48 26 36 40 10 42" fill="none" stroke="#fff" stroke-width="2.5" stroke-linecap="round"/>
  <polyline points="20,32 10,42 21,51" fill="none" stroke="#fff" stroke-width="2.5" stroke-linecap="round" stroke-linejoin="round"/>
</svg>

<div class="note note--body">Quicksand</div>
<svg class="note-arrow note-arrow--body" viewBox="0 0 60 60" aria-hidden="true">
  <path d="M44 4 C48 26 36 40 10 42" fill="none" stroke="#fff" stroke-width="2.5" stroke-linecap="round"/>
  <polyline points="20,32 10,42 21,51" fill="none" stroke="#fff" stroke-width="2.5" stroke-linecap="round" stroke-linejoin="round"/>
</svg>

</body>
</html>
```